Etiketten für Kürbiskernöl
Zielgruppe
Wir betreiben eine Landwirschaft, vorwiegend Ackerbau und Viehwirtschaft im nordöstlichen Niederösterreich. Wir sind ein reines Familienunternehmen. Unsere Zielgruppe ist 20 Jahre aufwärts, männlich wie weiblich und legt großen Wert auf Regionalität und hohe Qualität der Produkte.
Aufgabenstellung
Das Etikett wird für unsere Kürbiskernölflasche benötigt. Die Vorderseite soll unseren Namen, Produktbezeichnung und Füllmenge enthalten. Familie Wendtner - Kürbiskernöl 100% rein - 500ml Für die Rückseite gibt es einen entsprechenden Text (siehe Anhang).
Angehängt haben wir auch Etikett Vorderseiten, die uns sehr ansprechen. Es soll auf jeden Fall ein Kürbis abgebildet sein und ein hochwertiges, eher minimalistischen Design haben.
In Zukunft könnten wir uns auch vorstellen die Kürbiskerne in Form von Knabberkernen zu verkaufen, wofür wir das Etikettendesign gern abwandeln würden.
Farben: dunkelgrau/schwarz, weiß, dunkelgrün/oliv, beige
Flaschenform: Valmera 500ml siehe Foto

```html
<!DOCTYPE html>
<html lang="de">
<head>
<meta charset="utf-8">
<title>Kürbiskernöl – Etiketten Familie Wendtner</title>
<link href="https://fonts.googleapis.com/css2?family=Amatic+SC:wght@400;700&family=Montserrat:wght@400;500&display=swap" rel="stylesheet">
<style>
  :root {
    --canvas: #f4f3ee;
    --label: #1c1b1b;
    --ink: #f5f3ee;
    --gold: #d6bd83;
    --gold-deep: #a88c52;
    --band: #d9c28b;
    --band-ink: #2a2620;
  }
  * { margin: 0; padding: 0; box-sizing: border-box; }
  html, body {
    width: 1200px; height: 600px; overflow: hidden;
    background: var(--canvas);
  }
  .sheet {
    position: relative; width: 1200px; height: 600px;
    display: flex; justify-content: center; align-items: center; gap: 22px;
  }
  .label {
    position: relative; width: 190px; height: 560px;
    background: var(--label); color: var(--ink);
    font-family: "Montserrat", sans-serif;
    overflow: hidden;
  }
  .label__copy {
    position: absolute; left: 17px; right: 16px;
    font-size: 8.2px; line-height: 10px; text-align: justify;
  }
  .label__claim {
    position: absolute; left: 0; right: 0; top: 78px;
    text-align: center; color: var(--gold);
    font-family: "Amatic SC", sans-serif; font-size: 16px; font-weight: 700; letter-spacing: 0.02em;
  }
  .label__details {
    position: absolute; left: 18px; right: 6px; top: 321px;
    font-size: 7.8px; line-height: 10.5px; white-space: nowrap;
  }
  .label__details p + p { margin-top: 9px; }
  .label__date {
    font-family: "Amatic SC", sans-serif; font-size: 12px; font-weight: 700; margin-left: 8px;
  }
  .label__art {
    position: absolute; top: 404px; height: 134px;
    background: radial-gradient(ellipse at 50% 60%, rgba(214,189,131,0.35), rgba(168,140,82,0.12) 60%, rgba(28,27,27,0) 78%);
  }
  .label__art--back { left: 7px; width: 106px; }
  .label__art--front { left: 5px; width: 182px; }
  .label__band {
    position: absolute; left: 0; right: 0; bottom: 0; height: 24px;
  }
  .label__band svg { position: absolute; inset: 0; width: 100%; height: 100%; }
  .label__band span {
    position: absolute; left: 0; right: 0; bottom: 4px; text-align: center;
    color: var(--band-ink); font-size: 7.4px; font-weight: 500; letter-spacing: 0.18em;
  }
  .brand {
    position: absolute; left: 0; right: 0; top: 30px; text-align: center;
    font-size: 9px; font-weight: 500; letter-spacing: 0.3em; padding-left: 0.3em;
    color: var(--ink);
  }
  .product {
    position: absolute; left: 0; right: 0; top: 142px; text-align: center;
    font-family: "Amatic SC", sans-serif; font-weight: 400;
    font-size: 58px; line-height: 52px; letter-spacing: 0.01em;
  }
  .product__purity {
    position: absolute; left: 0; right: 0; top: 269px; text-align: center;
    color: var(--gold); font-size: 8.6px; font-weight: 500; letter-spacing: 0.42em; padding-left: 0.42em;
  }
</style>
</head>
<body>
<main class="sheet">

  <section class="label label--back" aria-label="Rückseite">
    <p class="label__copy" style="top:27px;">Nur die besten Kürbiskerne aus unserem eigenen Anbau werden zu unserem g'sund, g'schmackig, guatem Kürbiskernöl verarbeitet.</p>
    <p class="label__claim">100% rein und naturbelassen</p>
    <p class="label__copy" style="top:120px;">Die Kürbiskerne werden schonend geröstet und in einem traditionellen Verfahren in einer regionalen Ölmühle kalt gepresst, was unserem Kürbiskernöl das einzigartige, intensiv-nussige Aroma verleiht.</p>
    <div class="label__details">
      <p>Familie Wendtner<br>2071 Lindenau 48</p>
      <p>Vor Wärme und Licht geschützt lagern.</p>
      <p>Mindestens haltbar bis:<span class="label__date">OKTOBER 2022</span></p>
    </div>
    <div class="label__art label__art--back" role="img" aria-label="Goldene Strichzeichnung eines Kürbisses"></div>
    <div class="label__band">
      <svg viewBox="0 0 190 24" preserveAspectRatio="none" aria-hidden="true">
        <path d="M0 4 L12 3 L26 5 L40 2 L58 4 L76 3 L94 5 L112 2 L130 4 L148 3 L166 5 L180 2 L190 4 L190 24 L0 24 Z" fill="var(--band)"/>
      </svg>
      <span>– 500 ML –</span>
    </div>
  </section>

  <section class="label label--front" aria-label="Vorderseite">
    <p class="brand">FAMILIE WENDTNER</p>
    <h1 class="product">KÜRBIS<br>KERNÖL</h1>
    <p class="product__purity">100% REIN</p>
    <div class="label__art label__art--front" role="img" aria-label="Goldene Strichzeichnung eines ganzen und eines aufgeschnittenen Kürbisses"></div>
    <div class="label__band">
      <svg viewBox="0 0 190 24" preserveAspectRatio="none" aria-hidden="true">
        <path d="M0 3 L14 5 L30 2 L46 4 L64 3 L82 5 L100 2 L118 4 L136 3 L154 5 L172 2 L190 4 L190 24 L0 24 Z" fill="var(--band)"/>
      </svg>
      <span>TRADITIONELL KALTGEPRESST</span>
    </div>
  </section>

</main>
</body>
</html>
```